チラシは対象のお子様の親に見て頂きます。(1番)
地域の保健師・相談員(このようなサービスを紹介する人)や保育所等の先生にも見られると思います。
こちらで作ったものをアレンジして頂きたいと思います。
全て使用しなくでも大丈夫です。
写真を使用していきたいのですが、いま題材がないので、ネットのサンプル画像を利用して頂けると幸いです。どのような写真があればいいか教えて頂ければ、弊社での撮影も可能です。
A4
片面
• 高解像度JPG (.jpg)
• イラストレーター形式 (.ai)

```html
<!DOCTYPE html>
<html lang="ja">
<head>
<meta charset="utf-8">
<title>保育所等訪問支援のご案内</title>
<link href="https://fonts.googleapis.com/css2?family=Zen+Maru+Gothic:wght@500;700;900&family=M+PLUS+Rounded+1c:wght@400;500;700;800&display=swap" rel="stylesheet">
<style>
:root{
  --cream:#fbf5e4;
  --paper:#ffffff;
  --brown:#5e3d22;
  --text:#4a3a2c;
  --orange:#ea8a2e;
  --orange-soft:#fbe2c4;
  --yellow:#f7d84c;
  --green:#6fae55;
  --line:#e3cfa9;
}
*{margin:0;padding:0;box-sizing:border-box}
html,body{width:849px;height:1200px;overflow:hidden;background:var(--cream)}
body{font-family:"M PLUS Rounded 1c",sans-serif;color:var(--text);position:relative}
.flyer{position:absolute;inset:0;background:var(--cream);overflow:hidden}
.abs{position:absolute}

.law-tag{left:22px;top:30px;width:110px;text-align:center}
.law-tag .small{display:inline-block;background:var(--orange);color:#fff;font-size:11px;font-weight:700;padding:2px 10px;border-radius:10px}
.law-tag .name{display:block;margin-top:4px;font-size:17px;font-weight:800;color:var(--green);background:#fff;border:2px solid var(--green);border-radius:6px;padding:3px 4px;line-height:1.25}
.lead{left:240px;top:12px;width:560px;text-align:center;font-size:17px;font-weight:700;color:var(--brown);letter-spacing:.04em}

.headline{left:140px;right:52px;top:44px;font-family:"Zen Maru Gothic",sans-serif;font-weight:900;color:var(--brown);line-height:1.2;text-align:right;white-space:nowrap}
.headline span{display:inline-block;background:linear-gradient(transparent 62%,var(--yellow) 62%)}
.headline .l1{font-size:38px}
.headline .l2{font-size:46px;margin-top:8px;letter-spacing:.04em}

.worries{left:42px;top:188px;width:425px;height:212px;background:var(--paper);border-radius:18px;border:2px dashed var(--line);padding:24px 24px}
.worries li{list-style:none;display:flex;align-items:center;gap:10px;font-size:19px;font-weight:700;color:var(--brown);margin-bottom:14px;white-space:nowrap}
.worries li svg{flex:none}
.worries-note{left:42px;top:410px;width:425px;font-size:12px;line-height:1.6;color:var(--text);text-align:center}

.flow-label{left:508px;top:188px;width:30px;height:420px;border-right:3px solid var(--orange);padding-right:6px;padding-top:6px}
.flow-label span{display:block;writing-mode:vertical-rl;font-size:20px;font-weight:800;color:var(--orange);letter-spacing:.2em}
.flow{left:552px;top:184px;width:254px}
.step{background:var(--paper);border-radius:10px;border:2px solid var(--orange-soft);padding:6px 10px;margin-bottom:14px;position:relative}
.step:not(:last-child)::after{content:"";position:absolute;left:50%;bottom:-13px;margin-left:-7px;border:7px solid transparent;border-top:7px solid var(--orange)}
.step h3{font-size:15px;font-weight:800;color:var(--orange);display:flex;align-items:center;gap:6px}
.step h3 span{background:var(--orange);color:#fff;border-radius:4px;font-size:13px;width:20px;height:20px;display:inline-flex;align-items:center;justify-content:center}
.step p{font-size:10px;line-height:1.45;margin-top:3px}

.photo{border-radius:14px;background:linear-gradient(135deg,#f3d9bf,#e8c3a0 55%,#cfb08c)}
.photo-parent{left:240px;top:462px;width:260px;height:150px;border-radius:50% 50% 46% 54%/55% 50% 50% 45%}
.photo-kids{left:425px;top:622px;width:381px;height:180px;background:linear-gradient(135deg,#d9ead0,#f1dcc0)}

.about{left:28px;top:620px;width:382px}
.about h2{font-family:"Zen Maru Gothic",sans-serif;font-size:22px;font-weight:900;color:var(--brown)}
.about h2 em{font-style:normal;font-size:15px}
.about p{font-size:11.5px;line-height:1.6;margin-top:6px;padding-left:14px;text-indent:-14px}
.about p::before{content:"● ";color:var(--orange);font-size:9px}
.about b{color:var(--orange)}
.about h4{font-size:14px;font-weight:800;color:var(--brown);margin-top:14px;display:flex;align-items:center;gap:6px}
.about h4::before{content:"";width:10px;height:10px;border-radius:50%;background:var(--green)}
.about .body{font-size:11.5px;line-height:1.6;margin-top:3px;padding-left:16px}

.service{top:814px;width:180px}
.service .photo{height:62px;border-radius:10px}
.service .tag{display:inline-block;margin-top:6px;font-size:13px;font-weight:800;color:#fff;padding:2px 12px;border-radius:12px}
.service p{font-size:10px;line-height:1.45;margin-top:4px}
.svc-day{left:425px}
.svc-day .tag{background:var(--green)}
.svc-visit{left:622px}
.svc-visit .tag{background:var(--orange)}

.map{left:425px;top:955px;width:180px;height:180px;background:#eef0e6;border:2px solid var(--line);border-radius:8px}
.contact{left:622px;top:955px;width:190px}
.brand{display:flex;align-items:center;gap:6px;font-size:16px;font-weight:800;color:var(--brown);white-space:nowrap}
.brand i{width:14px;height:14px;border-radius:50%;background:var(--green);display:block}
.contact .addr{font-size:10.5px;line-height:1.5;margin-top:8px}
.contact .tel{display:flex;align-items:center;gap:5px;font-size:20px;font-weight:800;color:var(--brown);margin-top:4px}
.contact .fax{font-size:11px;font-weight:700}
.contact .hours{font-size:10.5px;line-height:1.5;margin-top:6px}
</style>
</head>
<body>
<div class="flyer">

  <div class="abs law-tag"><span class="small">児童福祉法</span><span class="name">保育所等<br>訪問支援</span></div>
  <p class="abs lead">発達支援が必要なお子様、そのご家族の皆様へ</p>

  <h1 class="abs headline"><span class="l1">専門職の私たちがご自宅を訪問して</span><br><span class="l2">個別療育を行います。</span></h1>

  <ul class="abs worries">
    <li><svg width="20" height="20" viewBox="0 0 20 20"><rect x="1" y="1" width="18" height="18" rx="4" fill="none" stroke="#ea8a2e" stroke-width="2"/><path d="M5 10l4 4 7-9" fill="none" stroke="#ea8a2e" stroke-width="2.5" stroke-linecap="round"/></svg>お友達となかなか遊べない</li>
    <li><svg width="20" height="20" viewBox="0 0 20 20"><rect x="1" y="1" width="18" height="18" rx="4" fill="none" stroke="#ea8a2e" stroke-width="2"/><path d="M5 10l4 4 7-9" fill="none" stroke="#ea8a2e" stroke-width="2.5" stroke-linecap="round"/></svg>活動に集中できず、参加が難しい</li>
    <li><svg width="20" height="20" viewBox="0 0 20 20"><rect x="1" y="1" width="18" height="18" rx="4" fill="none" stroke="#ea8a2e" stroke-width="2"/><path d="M5 10l4 4 7-9" fill="none" stroke="#ea8a2e" stroke-width="2.5" stroke-linecap="round"/></svg>行事への参加が難しい</li>
    <li><svg width="20" height="20" viewBox="0 0 20 20"><rect x="1" y="1" width="18" height="18" rx="4" fill="none" stroke="#ea8a2e" stroke-width="2"/><path d="M5 10l4 4 7-9" fill="none" stroke="#ea8a2e" stroke-width="2.5" stroke-linecap="round"/></svg>勉強が苦手でついて行けない</li>
  </ul>
  <p class="abs worries-note">…など集団での生活の場での困りごとについて、<br>訪問して一緒に考えてお手伝いします。</p>

  <div class="abs flow-label"><span>ご利用の流れ</span></div>
  <div class="abs flow">
    <div class="step"><h3><span>1</span>相談</h3><p>お電話でお気軽にご相談ください。お子さまの様子をお聞きします。</p></div>
    <div class="step"><h3><span>2</span>保育所先への説明・同意</h3><p>訪問先へサービス内容を説明し、同意をいただきます。</p></div>
    <div class="step"><h3><span>3</span>サービス申請・手続き</h3><p>市町村の窓口で受給者証の申請を行います。</p></div>
    <div class="step"><h3><span>4</span>個別支援計画の作成</h3><p>ご家族と相談しながら支援の計画を作ります。</p></div>
    <div class="step"><h3><span>5</span>サービスの開始</h3></div>
  </div>

  <div class="abs photo photo-parent" role="img" aria-label="お母さんと子どもが寄り添う写真"></div>
  <div class="abs photo photo-kids" role="img" aria-label="手をつないで遊ぶ子どもたちの写真"></div>

  <section class="abs about">
    <h2>「保育所等訪問支援」<em>とは</em></h2>
    <p>お子さんが集団生活に適応できるように、お子さんの様子やその集団の環境に応じて、直接的に支援を行います。</p>
    <p>支援内容に関しては、保護者の要望だけでなく、訪問先の先生方の意見も大切にします。</p>
    <p>訪問には、お子さんの支援に必要な知識のある<b>専門職（作業療法士、保育士、児童指導員など）</b>が伺います。</p>
    <h4>対象となる方</h4>
    <div class="body">保育園、幼稚園、認定こども園、小学校、中学校、特別支援学校、放課後児童クラブなどに通う、集団生活に支援が必要なお子さん</div>
    <h4>頻度はどのくらい</h4>
    <div class="body">原則、月に１、２回</div>
    <h4>情報共有できます</h4>
    <div class="body">訪問時の様子は、保護者の方へ連絡帳などで共有します。</div>
  </section>

  <div class="abs service svc-day">
    <div class="photo" role="img" aria-label="通所施設での活動の写真"></div>
    <span class="tag">通所支援</span>
    <p>教室に通って、個別や小集団で療育を受けられます。</p>
  </div>
  <div class="abs service svc-visit">
    <div class="photo" role="img" aria-label="ご自宅での訪問支援の写真"></div>
    <span class="tag">訪問支援</span>
    <p>専門職がご自宅や園に伺い、療育を行います。</p>
  </div>

  <div class="abs map" role="img" aria-label="事業所までの案内地図"></div>

  <div class="abs contact">
    <div class="brand"><i></i>ひだまり支援室 ソラ</div>
    <p class="addr">〒000-0000<br>福岡県みどり市若葉町 123-4</p>
    <p class="tel"><svg width="18" height="18" viewBox="0 0 24 24"><path d="M6.6 10.8a15 15 0 006.6 6.6l2.2-2.2a1 1 0 011-.25 11.4 11.4 0 003.6.57 1 1 0 011 1V20a1 1 0 01-1 1A17 17 0 013 4a1 1 0 011-1h3.5a1 1 0 011 1 11.4 11.4 0 00.57 3.6 1 1 0 01-.25 1z" fill="#5e3d22"/></svg>0940-00-1234</p>
    <p class="fax">FAX 0940-00-1235</p>
    <p class="hours">営業時間<br>8:30〜17:30<br>休業日　日・祝</p>
  </div>

</div>
</body>
</html>
```